Flyer DesignFESTIVE, FLORISTRY WORKSHOP

WE NEED A FLYER, TO SEND OUT TO PROSPECTIVE CUSTOMERS, TO ATTEND A ONE DAY CHRISTMAS WORKSHOP, ALL MATERIALS WILL BE SUPPLIED AND SO TO WE WILL PROVIDE REFRESHMENTS, PARTICIPIANTS JUST NEED TO BRING THIER FLORISTRY SCISSORS

ON THE DAY THE WILL PARTICIPIATE IN CREATING SEASONAL FLORISTRY DESIGNS THAT THEY CAN BRING HOME TO LAST THE FESTIVE SEASON,

MARGOT AND BEATRIX WILL BE THERE WITH SOME UNIQUE IDEAS TO ENHANCE OUR CHRISTMAS FESTIVITIES. TOTAL COST FOR THE DAY IS £79.00. AND THE DATE IS 6THDECEMBER, 2014, AT THE GILDEN LODGE HARWICK, WHICH HAS ALSO A BUS LINK TO MANY OTHER AREAS, SO ENJOY YOURSELVES, GET INTO THE FESTIVE FEELING ON THIS SPECIAL OCCASION

Target Market(s)

FLOWER LOVERS THAT LIKE TO CREATE THIER OWN FLORAL DESIGNS

Industry/Entity Type

Hotel

Font styles to use
Decorative

Requirements
Must have
• A CHRISTMAS ATMOSPHERE, WITH A BEAUTIFUL DOOR WREATH AND TABLE DESIGN

BOTH TUTORS ON THE DAY ARE HIGHLY SKILLED, HIGHLY QUALIFIED, WITH BEATRIX, HAVING WON NGW BRAMFORD MEDAL,
Nice to have
• BETTER WORDING THAN I HAVE GIVEN YOU

telephone number 02881430526

```html
<!DOCTYPE html>
<html lang="en">
<head>
<meta charset="utf-8">
<title>Christmas Floristry Design – Creative Class</title>
<link rel="stylesheet" href="https://fonts.googleapis.com/css2?family=Just+Me+Again+Down+Here&family=Yanone+Kaffeesatz:wght@300;400&family=Didact+Gothic&family=Montserrat:wght@600;700&display=swap">
<style>
  :root {
    --backdrop: #9b1f45;
    --paper: #ffffff;
    --berry: #9c1d44;
    --holly-red: #d2232a;
    --tangerine: #ec6a1f;
    --gold: #f6c20f;
    --sage: #9bc465;
    --ink: #555555;
    --ink-dark: #333333;
  }
  * { box-sizing: border-box; margin: 0; padding: 0; }
  html, body { width: 900px; height: 1200px; overflow: hidden; }
  body { background: var(--backdrop); position: relative; font-family: "Didact Gothic", sans-serif; }

  .flyer {
    position: absolute; left: 47px; top: 316px;
    width: 806px; height: 568px;
    background: var(--paper); overflow: hidden;
  }

  .photo-tools {
    position: absolute; left: 0; top: 0; width: 290px; height: 165px;
    background: radial-gradient(ellipse at 40% 45%, #e3d6c6 0%, #f1e9e0 45%, rgba(255,255,255,0) 75%);
  }
  .photo-arrangement {
    position: absolute; right: 0; top: 0; width: 400px; height: 568px;
    background:
      radial-gradient(circle at 60% 38%, #c8102e 0%, #a8141f 18%, rgba(168,20,31,0) 34%),
      radial-gradient(circle at 55% 75%, #3b1b2b 0%, #4a2a36 14%, rgba(74,42,54,0) 30%),
      radial-gradient(circle at 85% 20%, #c9a06a 0%, rgba(201,160,106,0) 30%),
      linear-gradient(90deg, rgba(255,255,255,1) 0%, rgba(214,170,120,0.55) 22%, #b98857 55%, #8c5a3a 100%);
  }

  .title {
    position: absolute; left: 46px; top: 192px;
    font-family: "Just Me Again Down Here", cursive; font-weight: 400;
    line-height: 1; white-space: nowrap;
  }
  .title .line-one { display: block; color: var(--holly-red); font-size: 60px; }
  .title .line-two { display: block; font-size: 46px; margin-top: -2px; color: var(--berry); }
  .title .accent { color: var(--tangerine); }

  .badge {
    position: absolute; border-radius: 50%;
    border: 5px solid var(--paper);
    box-shadow: 0 2px 6px rgba(0,0,0,0.35);
    display: flex; flex-direction: column; align-items: center; justify-content: center;
    text-align: center; color: var(--paper);
  }
  .badge-price {
    left: 347px; top: 71px; width: 114px; height: 114px;
    background: var(--gold); color: #1a1a1a;
    font-family: "Yanone Kaffeesatz", sans-serif; font-weight: 300;
  }
  .badge-price .price-row { display: flex; align-items: flex-start; line-height: 1; }
  .badge-price .only { font-size: 16px; margin: 6px 3px 0 0; }
  .badge-price .amount { font-size: 50px; }
  .badge-price .per-day { font-size: 16px; margin-top: -4px; margin-left: 18px; }

  .badge-class {
    left: 269px; top: 155px; width: 136px; height: 136px;
    background: var(--berry);
  }
  .badge-class .script { font-family: "Just Me Again Down Here", cursive; font-size: 30px; line-height: 0.9; }
  .badge-class .word { font-family: "Yanone Kaffeesatz", sans-serif; font-weight: 300; font-size: 48px; line-height: 1; }

  .badge-coach {
    left: 402px; top: 404px; width: 154px; height: 154px;
    background: var(--sage);
  }
  .badge-coach .script { font-family: "Just Me Again Down Here", cursive; font-size: 30px; line-height: 1; }
  .badge-coach .word { font-family: "Yanone Kaffeesatz", sans-serif; font-weight: 300; font-size: 28px; line-height: 1.02; }

  .intro { position: absolute; left: 45px; top: 322px; width: 362px; font-size: 12px; line-height: 1.3; color: var(--ink); }
  .intro p + p { margin-top: 12px; }
  .tutor { color: var(--holly-red); font-weight: 700; font-family: "Montserrat", sans-serif; font-size: 11px; }

  .details { position: absolute; left: 45px; top: 455px; font-size: 12px; line-height: 14px; color: var(--ink); }
  .details strong { font-family: "Montserrat", sans-serif; font-weight: 700; font-size: 11px; color: var(--ink-dark); }
  .details .fee { color: var(--holly-red); }

  .phone { position: absolute; left: 45px; top: 502px; display: flex; align-items: center; gap: 6px; }
  .phone-number { font-family: "Montserrat", sans-serif; font-weight: 700; font-size: 26px; color: var(--tangerine); letter-spacing: 0.5px; line-height: 1; }
</style>
</head>
<body>
  <main class="flyer">
    <div class="photo-tools" role="img" aria-label="Photo of floristry secateurs, a ball of twine and an orange flower"></div>
    <div class="photo-arrangement" role="img" aria-label="Photo of a Christmas table arrangement with red roses, gold pine cones, berries and grapes"></div>

    <h1 class="title">
      <span class="line-one">Christmas</span>
      <span class="line-two">Floristry <span class="accent">Design</span></span>
    </h1>

    <div class="badge badge-price">
      <div class="price-row"><span class="only">Only</span><span class="amount">£79</span></div>
      <span class="per-day">per day</span>
    </div>

    <div class="badge badge-class">
      <span class="script">Creative</span>
      <span class="word">Class</span>
    </div>

    <section class="intro">
      <p>Come and join us to participate in creating seasonal floristry design. Just bring together your floristry scissors and we will supply all materials for you. Design with us and bring it home and decorate it at your special place.</p>
      <p>Our professional florist <span class="tutor">MARGOT</span> and <span class="tutor">BEATRIX</span> will share with you the uniques ideas to enhance your Christmas Festivities.</p>
    </section>

    <section class="details">
      <p>Fee <strong class="fee">£79</strong> per day</p>
      <p>Date: <strong>6th December, 2014,</strong></p>
      <p>Venue: <strong>GILDEN LODGE HARWICK</strong></p>
    </section>

    <div class="phone">
      <svg class="phone-icon" width="26" height="26" viewBox="0 0 28 28" aria-hidden="true">
        <circle cx="14" cy="14" r="12.5" fill="none" stroke="#555" stroke-width="1.6"/>
        <path d="M10 7.5c-1 .6-2 1.8-1.6 3.6.8 3.4 4 7.6 7.2 9.2 1.6.8 3 .2 3.8-.6l.6-.7-2.6-2.4-1.4 1c-1.6-.6-3.8-3.4-4.2-5.2l1.2-1.2-2-3.2z" fill="none" stroke="#555" stroke-width="1.5" stroke-linejoin="round"/>
      </svg>
      <span class="phone-number">02881430526</span>
    </div>

    <div class="badge badge-coach">
      <span class="script">Coached by</span>
      <span class="word">Professionals</span>
      <span class="word">Florist</span>
    </div>
  </main>
</body>
</html>
```